Business Card Design

New business card design

Target Market(s)

Residential & Commercial Property Managers

Industry/Entity Type

Plumbing Services

Contact Information for Business Card

Name - Owen Tredgold, title - Director, Phone Number - 0431 862 507, email - owen@rvb-plumbing.com.au, Company ABN - 73 215 904 386,

Font styles to use
Sans Serif

Colors
0054AA
0677BA
7BADD7
CADEEF
E8F1F8

```html
<!DOCTYPE html>
<html lang="en">
<head>
<meta charset="utf-8">
<title>RVB Plumbing Services – Business Card</title>
<link rel="stylesheet" href="https://fonts.googleapis.com/css2?family=Fira+Sans+Condensed:wght@300;400;600&display=swap">
<style>
  :root {
    --stage: #d9dde3;
    --card-dark: #23272e;
    --card-dark-2: #2d323a;
    --card-light: #ffffff;
    --ink: #2b2f36;
    --ink-soft: #5a5f66;
    --tagline-dark: #8a8378;
    --accent: #1aa2e2;
  }
  * { box-sizing: border-box; margin: 0; padding: 0; }
  html, body {
    width: 1200px; height: 675px; overflow: hidden;
    background: var(--stage);
    font-family: "Fira Sans Condensed", sans-serif;
  }
  .stage {
    position: relative; width: 1200px; height: 675px;
    display: flex; align-items: center; justify-content: center; gap: 60px;
  }
  .card {
    position: relative; width: 500px; height: 306px;
    box-shadow: 0 10px 30px rgba(30, 40, 55, 0.25);
    overflow: hidden;
  }
  .card--front { background: var(--card-dark); }
  .droplet-texture {
    position: absolute; inset: 0;
    background: radial-gradient(ellipse at 40% 35%, var(--card-dark-2), var(--card-dark) 75%);
  }
  .brand {
    position: absolute; left: 0; right: 0;
    display: flex; align-items: center; justify-content: center; gap: 10px;
  }
  .brand__name {
    font-weight: 300; font-size: 96px; line-height: 1; letter-spacing: 2px;
  }
  .brand__dot {
    width: 18px; height: 18px; border-radius: 50%; background: var(--accent);
    align-self: flex-end; margin-bottom: 12px;
  }
  .tagline {
    position: absolute; left: 0; right: 0; text-align: center;
    font-weight: 300; font-size: 13px; letter-spacing: 11px;
  }
  .card--front .brand { top: 78px; }
  .card--front .brand__name { color: #ffffff; }
  .card--front .tagline { top: 196px; color: var(--tagline-dark); }

  .card--back { background: var(--card-light); }
  .card--back .brand { top: 36px; }
  .card--back .brand__name { color: var(--ink); font-size: 84px; }
  .card--back .tagline { top: 134px; color: var(--ink-soft); font-size: 12px; }
  .details {
    position: absolute; top: 172px; left: 0; right: 0;
    display: flex; justify-content: center; align-items: center; gap: 14px;
  }
  .person { text-align: right; }
  .person__name { color: var(--accent); font-weight: 600; font-size: 24px; line-height: 1.05; }
  .person__title { color: var(--ink); font-size: 14px; }
  .divider { width: 1.5px; height: 66px; background: var(--ink); }
  .contacts { list-style: none; font-size: 13.5px; color: var(--ink); line-height: 1.55; }
  .contacts li { display: flex; align-items: center; gap: 6px; }
  .contacts svg { width: 11px; height: 11px; fill: var(--accent); flex: none; }
  .abn {
    position: absolute; top: 258px; left: 0; right: 0; text-align: center;
    font-size: 17px; color: var(--ink);
  }
  .abn__label { color: var(--accent); }
</style>
</head>
<body>
<main class="stage">
  <section class="card card--front" aria-label="Card front">
    <div class="droplet-texture" role="img" aria-label="Water droplets on a dark surface"></div>
    <div class="brand"><span class="brand__name">rvb</span><span class="brand__dot"></span></div>
    <p class="tagline">plumbing services</p>
  </section>

  <section class="card card--back" aria-label="Card back">
    <div class="brand"><span class="brand__name">rvb</span><span class="brand__dot"></span></div>
    <p class="tagline">plumbing services</p>
    <div class="details">
      <div class="person">
        <p class="person__name">Owen Tredgold</p>
        <p class="person__title">Director</p>
      </div>
      <span class="divider"></span>
      <ul class="contacts">
        <li><svg viewBox="0 0 24 24"><path d="M6.6 10.8a15.1 15.1 0 0 0 6.6 6.6l2.2-2.2a1 1 0 0 1 1-.25 11.4 11.4 0 0 0 3.6.57 1 1 0 0 1 1 1V20a1 1 0 0 1-1 1A17 17 0 0 1 3 4a1 1 0 0 1 1-1h3.5a1 1 0 0 1 1 1c0 1.25.2 2.45.57 3.6a1 1 0 0 1-.25 1z"/></svg>0431 862 507</li>
        <li><svg viewBox="0 0 24 24"><path d="M2 5h20v14H2z M2 5l10 8 10-8" /></svg>owen@rvb-plumbing.com.au</li>
        <li><svg viewBox="0 0 24 24"><circle cx="12" cy="12" r="10"/><path d="M2 12h20M12 2c3 3 3 17 0 20M12 2c-3 3-3 17 0 20" stroke="#fff" stroke-width="1.5" fill="none"/></svg>rvb-plumbing.com.au</li>
      </ul>
    </div>
    <p class="abn"><span class="abn__label">ABN</span> - 73 215 904 386</p>
  </section>
</main>
</body>
</html>
```